Flyer for Brand New Montessori School

Quiet Harbor Academy is opening in the fall to students infant-5th grade. We need a catchy, professional flyer that will attract a very upscale clientele. Most of our students will be under the age of 5, but we want to attract older students as well. The project is to design a flyer that tells people about our school, and directs them to the website to enroll/get more information

Target Market(s)

Upscale, affluent parents who need care for and want to educate their children starting at a young age.

Industry/Entity Type

Education/Day Care

Font styles to use
Serif

Colors
59FF00
82FF00
B8FF75
E3FFCB
F4FFEA
6B429C
8869AF
B7A5CE
E3DAEB
F3F0F8

Requirements
Must have
• photos of children, a clean look
Nice to have
• Please see attached logo samples. I am going to use either 2a or 4a; those are the colors i would like to use
Should not have
• A cluttered look or too much information

```html
<!DOCTYPE html>
<html lang="en">
<head>
<meta charset="utf-8">
<title>Quiet Harbor Academy – Flyer</title>
<link href="https://fonts.googleapis.com/css2?family=Poppins:wght@300;400;600;700&display=swap" rel="stylesheet">
<style>
  :root{
    --stage:#d9d9d9;
    --paper:#ffffff;
    --green:#2aa53b;
    --purple-deep:#4e2578;
    --purple:#6b429c;
    --purple-ink:#4b2278;
    --ink:#2a2a2a;
    --white:#ffffff;
    --books-light:#efe6c8;
    --books-mid:#c9b27a;
    --books-dark:#6e5a3a;
  }
  html,body{margin:0;padding:0;width:1090px;height:1200px;overflow:hidden;background:var(--stage);}
  .flyer{
    position:absolute;left:139px;top:74px;width:1365px;height:1766px;
    transform:scale(.5953);transform-origin:0 0;background:var(--paper);
    font-family:"Poppins",sans-serif;color:var(--ink);overflow:hidden;
  }
  .flyer-art{position:absolute;left:0;top:0;width:1365px;height:1766px;}
  .headline{
    position:absolute;left:80px;top:66px;margin:0;width:650px;
    font-weight:700;font-size:35px;line-height:43px;color:var(--white);
  }
  .tagline{
    position:absolute;left:80px;top:182px;margin:0;width:640px;
    font-weight:300;font-size:39px;line-height:48px;color:var(--white);text-transform:uppercase;
  }
  .intro-column{position:absolute;left:80px;top:740px;width:570px;}
  .lead{margin:0 0 24px;font-weight:700;font-size:21px;line-height:27px;color:var(--purple-ink);}
  .lead a{color:inherit;text-decoration:underline;}
  .body-copy{margin:0 0 24px;font-size:19px;line-height:24.2px;}
  .brand{
    position:absolute;left:80px;top:1592px;display:flex;align-items:center;gap:10px;
  }
  .brand-dot{width:66px;height:66px;border-radius:50%;background:var(--purple);}
  .brand-name{font-weight:700;font-size:32px;line-height:34px;color:var(--purple-ink);}
  .contact{position:absolute;left:80px;top:1696px;margin:0;font-weight:700;font-size:26px;line-height:32px;color:var(--ink);white-space:nowrap;}
  .features{position:absolute;left:742px;top:698px;width:572px;color:var(--white);}
  .features-title{margin:0 0 34px;width:545px;font-weight:700;font-size:25px;line-height:33px;}
  .feature{margin-bottom:36px;}
  .feature-head{display:flex;align-items:flex-start;gap:29px;margin-bottom:11px;height:72px;}
  .feature-icon{width:72px;height:72px;flex:none;}
  .feature-title{margin:2px 0 0;width:360px;font-weight:700;font-size:27px;line-height:32px;}
  .feature-list{margin:0;padding:0 0 0 30px;font-size:19.5px;line-height:29px;}
</style>
</head>
<body>
<div class="flyer">
  <svg class="flyer-art" viewBox="0 0 1365 1766" xmlns="http://www.w3.org/2000/svg">
    <defs>
      <linearGradient id="booksTone" x1="0" y1="0" x2="1" y2="1">
        <stop offset="0" stop-color="var(--books-light)"/>
        <stop offset=".55" stop-color="var(--books-mid)"/>
        <stop offset="1" stop-color="var(--books-dark)"/>
      </linearGradient>
      <linearGradient id="readerTone" x1="0" y1="0" x2="1" y2="1">
        <stop offset="0" stop-color="#5b4030"/>
        <stop offset=".6" stop-color="#9a6a44"/>
        <stop offset="1" stop-color="#3a2a22"/>
      </linearGradient>
      <linearGradient id="studentTone" x1="0" y1="0" x2="0" y2="1">
        <stop offset="0" stop-color="#9a8a7c"/>
        <stop offset=".6" stop-color="#c9a48a"/>
        <stop offset="1" stop-color="#2e3c66"/>
      </linearGradient>
      <linearGradient id="panelTone" x1="0" y1="0" x2="1" y2="1">
        <stop offset="0" stop-color="var(--purple-deep)"/>
        <stop offset=".5" stop-color="#5f3590"/>
        <stop offset="1" stop-color="var(--purple)"/>
      </linearGradient>
    </defs>
    <rect x="0" y="0" width="1365" height="740" fill="url(#booksTone)" role="img" aria-label="Photo of an open book with fanned pages"/>
    <polygon points="0,307 525,307 170,705 0,732" fill="url(#readerTone)" role="img" aria-label="Photo of a girl working on a laptop in a library"/>
    <polygon points="525,307 632,307 1095,563 716,625 170,705" fill="url(#studentTone)" role="img" aria-label="Photo of a smiling schoolboy in glasses and uniform"/>
    <polygon points="0,732 170,705 716,625 716,1766 0,1766" fill="var(--paper)"/>
    <polygon points="716,625 1095,563 1336,695 1336,1766 716,1766" fill="url(#panelTone)" role="img" aria-label="Purple-tinted photo of a student writing"/>
    <polygon points="1336,695 1365,710 1365,1766 1336,1766" fill="var(--paper)"/>
    <line x1="525" y1="307" x2="170" y2="705" stroke="var(--paper)" stroke-width="5"/>
    <line x1="632" y1="307" x2="1365" y2="710" stroke="var(--paper)" stroke-width="5"/>
    <path d="M0,0 H380 L740,60 C830,95 830,210 770,262 C735,292 715,307 690,307 H0 Z" fill="var(--green)"/>
  </svg>

  <h1 class="headline">Give your child an advanced start at Quiet Harbor Academy!</h1>
  <p class="tagline">Montessori education for tomorrow’s global leaders</p>

  <section class="intro-column">
    <p class="lead">Quiet Harbor Academy educates infant through 5th grade students, utilizing the renowned Montessori approach to education. Montessori education helped students develop skills and talents that lead to incredible future success. (Check out list of <a>successful Montessori alumni!</a>)</p>
    <p class="body-copy">Our students achieve academic excellence, learn independence and discover a natural love for learning. Students develop respect for self and others and a global mindset. We employ a research-based, neurologically informed educational program that promotes brain development, social skills, problem solving and creativity. We want to capitalize on the growth of young minds and challenge students to achieve their potential. We expect that our students will achieve success and change the world.</p>
    <p class="body-copy">Students are taught in a manner that allows each one to accept new challenges once they have mastered a skill. Students are allowed to grow and advance at their own pace and are encouraged to try new things. In addition to core academic subjects, students also have classes in Art, Music, Physical Education, Language and Life Skills.</p>
    <p class="body-copy">Our teachers are experienced and caring professionals who are experts in their field. We searched far and wide to find THE BEST educators to teach our students.</p>
    <p class="body-copy">Enroll your child today and give them the gift of an advanced start to their educational journey.</p>
  </section>

  <div class="brand">
    <div class="brand-dot"></div>
    <div class="brand-name">QUIET HARBOR<br>ACADEMY</div>
  </div>
  <p class="contact">www.quietharbor.com | + 0000 000 000</p>

  <section class="features">
    <h2 class="features-title">Key Characteristics that differentiate Quiet Harbor Academy:</h2>

    <div class="feature">
      <div class="feature-head">
        <svg class="feature-icon" viewBox="0 0 72 72"><path d="M0,16 Q0,0 16,0 H48 Q72,0 72,36 Q72,72 48,72 H16 Q0,72 0,56 Z" fill="var(--green)"/><path d="M16,26 L34,18 L52,26 L34,34 Z" fill="#fff"/><rect x="18" y="38" width="32" height="6" fill="#fff"/><rect x="16" y="46" width="34" height="6" fill="#fff"/><rect x="18" y="54" width="32" height="6" fill="#fff"/></svg>
        <h3 class="feature-title">Customized Educational Program</h3>
      </div>
      <ul class="feature-list">
        <li>Begin with infants-utilize every precious moment</li>
        <li>Montessori Curriculum</li>
        <li>Critical thinking, Creativity, Academic Skill</li>
        <li>Problem Solving, Language, Compassion</li>
        <li>Research and Neurologically based</li>
      </ul>
    </div>

    <div class="feature">
      <div class="feature-head">
        <svg class="feature-icon" viewBox="0 0 72 72"><path d="M0,16 Q0,0 16,0 H48 Q72,0 72,36 Q72,72 48,72 H16 Q0,72 0,56 Z" fill="var(--green)"/><circle cx="22" cy="24" r="6" fill="#fff"/><circle cx="36" cy="28" r="6" fill="#fff"/><circle cx="50" cy="24" r="6" fill="#fff"/><path d="M12,48 Q12,33 22,33 Q30,33 30,44 V48 Z M28,54 Q28,38 36,38 Q44,38 44,54 Z M42,48 V44 Q42,33 50,33 Q60,33 60,48 Z" fill="#fff"/></svg>
        <h3 class="feature-title">Family<br>Support</h3>
      </div>
      <ul class="feature-list">
        <li>Welcoming atmosphere for parents as partners</li>
        <li>Provide answers for parents in all areas of parenting</li>
        <li>Create community of like-minded parents</li>
        <li>High levels of customer service</li>
        <li>Engage other caring adults and multi-generational families</li>
        <li>Redefine expectations for education</li>
        <li>Help student acheive potential</li>
      </ul>
    </div>

    <div class="feature">
      <div class="feature-head">
        <svg class="feature-icon" viewBox="0 0 72 72"><path d="M0,16 Q0,0 16,0 H48 Q72,0 72,36 Q72,72 48,72 H16 Q0,72 0,56 Z" fill="var(--green)"/><circle cx="34" cy="28" r="14" fill="none" stroke="#fff" stroke-width="3"/><path d="M28,42 H40 V50 H28 Z" fill="#fff"/><rect x="30" y="53" width="8" height="4" fill="#fff"/></svg>
        <h3 class="feature-title">Top Notch<br>Team</h3>
      </div>
      <ul class="feature-list">
        <li>Talented, best in class professional teachers</li>
        <li>Team that is balanced around desired characteristics</li>
        <li>Opportunity to provide input and shape future of the</li>
        <li>school</li>
        <li>Great compenstation, profit sharing and robust professional development opportunities</li>
        <li>Experienced school leader with 25+ years experience in best schools in the country</li>
      </ul>
    </div>
  </section>
</div>
</body>
</html>
```